Snapframe Party Rentals New Business Card*

Need a business card designed for a Photo Booth Hire company.Must look very professional and colorful.A new creative logo would be a bonus. Our current logo is attached on here.

Contact Information for Business Card

Business Name: SNAPFRAME PARTY RENTALS
Contact Person: MARCUS OKAFOR
Mobile: 0491826350
Email: INFO@SNAPFRAMERENTALS.EXAMPLE
Website: WWW.SNAPFRAMERENTALS.EXAMPLE
Facebook: WWW.SOCIALPAGE.EXAMPLE/SNAPFRAME.RNT

Font styles to use
Serif
Sans Serif
Script

Colors

Designer to choose colors to be used in the design.

Requirements
Must have
• Bonus if the colors match our website.

```html
<!DOCTYPE html>
<html lang="en">
<head>
<meta charset="utf-8">
<title>Snapframe Party Rentals – Business Card</title>
<link rel="stylesheet" href="https://fonts.googleapis.com/css2?family=Roboto+Condensed:wght@400;700&family=Roboto:wght@400&display=swap">
<style>
  :root {
    --backdrop: #d9d9d9;
    --card-front: #2c2c2e;
    --card-back: #232325;
    --ink-white: #ffffff;
    --ink-grey: #b9b9b9;
    --rule: #77777a;
  }
  html, body {
    margin: 0;
    padding: 0;
    width: 1200px;
    height: 1108px;
    overflow: hidden;
    background: var(--backdrop);
  }
  .stage {
    position: relative;
    width: 1200px;
    height: 1108px;
    display: flex;
    align-items: center;
    justify-content: center;
    gap: 60px;
  }
  .card {
    width: 440px;
    height: 680px;
    border-radius: 26px;
    box-sizing: border-box;
    position: relative;
  }
  .card--front {
    background: var(--card-front);
    display: flex;
    flex-direction: column;
    align-items: center;
    padding-top: 92px;
    color: var(--ink-white);
    text-align: center;
  }
  .brand-mark {
    width: 120px;
    height: 120px;
    border-radius: 50%;
    background: var(--ink-white);
    margin-bottom: 34px;
  }
  .brand-name {
    font-family: "Roboto Condensed", sans-serif;
    font-weight: 700;
    font-size: 30px;
    line-height: 1.02;
    letter-spacing: 1px;
    margin: 0;
  }
  .brand-url {
    font-family: "Roboto Condensed", sans-serif;
    font-weight: 700;
    font-size: 13.5px;
    letter-spacing: 0.6px;
    margin: 6px 0 0;
  }
  .person {
    margin-top: 58px;
    font-family: "Roboto", sans-serif;
    color: var(--ink-grey);
  }
  .person__name {
    font-size: 25px;
    letter-spacing: 1.5px;
    margin: 0;
  }
  .person__phone {
    font-size: 23px;
    letter-spacing: 1.5px;
    margin: 4px 0 0;
  }
  .contact-divider {
    display: flex;
    align-items: center;
    gap: 8px;
    width: 290px;
    margin-top: 14px;
  }
  .contact-divider__line {
    flex: 1;
    height: 1px;
    background: var(--rule);
  }
  .contact-divider__icons {
    display: flex;
    gap: 5px;
  }
  .contact-list {
    list-style: none;
    margin: 10px 0 0;
    padding: 0;
    font-family: "Roboto", sans-serif;
    font-size: 15.5px;
    line-height: 1.45;
    color: var(--ink-white);
  }
  .contact-list__rule {
    width: 290px;
    height: 1px;
    background: var(--rule);
    margin-top: 8px;
  }
  .card--back {
    background: var(--card-back);
  }
  .back-mark {
    position: absolute;
    left: 50%;
    top: 440px;
    transform: translateX(-50%);
    display: flex;
    flex-direction: column;
    align-items: center;
    gap: 10px;
  }
  .back-mark__dot {
    width: 40px;
    height: 40px;
    border-radius: 50%;
    background: var(--ink-white);
  }
  .back-mark__name {
    font-family: "Roboto Condensed", sans-serif;
    font-weight: 700;
    font-size: 12px;
    letter-spacing: 1px;
    color: var(--ink-white);
    white-space: nowrap;
  }
</style>
</head>
<body>
<main class="stage">
  <section class="card card--front">
    <div class="brand-mark" aria-hidden="true"></div>
    <h1 class="brand-name">SNAPFRAME<br>PARTY RENTALS</h1>
    <p class="brand-url">WWW.SNAPFRAMERENTALS.EXAMPLE</p>

    <div class="person">
      <p class="person__name">MARCUS OKAFOR</p>
      <p class="person__phone">0491826350</p>
    </div>

    <div class="contact-divider">
      <span class="contact-divider__line"></span>
      <span class="contact-divider__icons">
        <svg width="18" height="18" viewBox="0 0 18 18" aria-label="email">
          <rect x="1" y="4" width="16" height="11" fill="#fff"/>
          <path d="M1 4 L9 10 L17 4" fill="none" stroke="#2c2c2e" stroke-width="1.4"/>
        </svg>
        <svg width="18" height="18" viewBox="0 0 18 18" aria-label="website">
          <circle cx="9" cy="9" r="8" fill="#fff"/>
          <ellipse cx="9" cy="9" rx="3.5" ry="8" fill="none" stroke="#2c2c2e" stroke-width="1.2"/>
          <line x1="1" y1="9" x2="17" y2="9" stroke="#2c2c2e" stroke-width="1.2"/>
        </svg>
        <svg width="18" height="18" viewBox="0 0 18 18" aria-label="social page">
          <circle cx="9" cy="9" r="8" fill="#fff"/>
        </svg>
      </span>
      <span class="contact-divider__line"></span>
    </div>

    <ul class="contact-list">
      <li>info@snapframerentals.example</li>
      <li>www.snapframerentals.example</li>
      <li>www.socialpage.example/snapframe.rnt</li>
    </ul>
    <div class="contact-list__rule"></div>
  </section>

  <section class="card card--back">
    <div class="back-mark">
      <span class="back-mark__dot" aria-hidden="true"></span>
      <span class="back-mark__name">SNAPFRAME PARTY RENTALS</span>
    </div>
  </section>
</main>
</body>
</html>
```